Exclusive beauty salon needs a price list or services booklet

I need a new very attractive flyer for my beauty salon, containing information on the different services and their prices.
In attachment you can find a pdf of the "old" one, but I'd love to have a beautifully designed new one!
I'd love to have a booklet in format 148 x 148 mm, or in US format, containing 12 or 16 pages, but if you can offer other nice looking designs they are welcome!
The services that need to come in the booklet with their prices can all be found on my website: www.atelierv.be, starting with
Gelaatsverzorging
Wimperverlenging
Suikerontharing
Wimperlifting
Permanente Make Up
Airbrush Tanning

Target Market(s)

woman from 20 to 89 years old

Industry/Entity Type

Beauty Salon

Font styles to use
Sans Serif

Colors

Designer to choose colors to be used in the design.

Requirements
Must have
• a classy nice look, it must contain details about the services from my beauty salon and their prices, and nice pictures.
• The Names, prices and explanations of the services can easily be found on my website: www.atelierv.be
Nice to have
• In attachment you can find the "old" price list in pdf, what I need now is a "new booklet" with the new logo and updated services price list.
• I need a very nice and attractive looking booklet, classy chique, Paris chique, looking very expensive.
Should not have
• Not too much colors, not too curly, but still feminine

```html
<!DOCTYPE html>
<html lang="nl">
<head>
<meta charset="utf-8">
<title>Prijsboekje – Permanente make-up &amp; Airbrush tanning</title>
<link href="https://fonts.googleapis.com/css2?family=Raleway:wght@300;400;500;700;900&display=swap" rel="stylesheet">
<style>
:root{
  --bg:#e9e6e3;
  --blush:#f8d7df;
  --blush-soft:#fbe9ee;
  --rose:#e8a8b6;
  --rose-deep:#e39aac;
  --charcoal:#363233;
  --ink:#2a2627;
  --paper:#ffffff;
  --paper-warm:#fdf7f8;
  --sky:#a9cde6;
}
*{box-sizing:border-box;margin:0;padding:0}
html,body{width:1200px;height:1000px;overflow:hidden}
body{background:var(--bg);font-family:'Raleway',sans-serif;color:var(--ink);position:relative}
.page{position:absolute;overflow:hidden}
.abs{position:absolute}
.page-number{position:absolute;bottom:0;width:24px;height:24px;background:var(--rose);color:#fff;font-size:8px;font-weight:700;display:flex;align-items:center;justify-content:center}

/* spread 1 */
.page--eyes{left:132px;top:18px;width:468px;height:467px;background:var(--blush)}
.page--eyes .photo-band{position:absolute;left:311px;top:0;width:157px;height:100%;background:var(--charcoal)}
.page--brows{left:600px;top:18px;width:468px;height:467px;background:var(--paper)}
.photo-frame{position:absolute;border:3px solid #fff;background:var(--paper)}
.photo-frame .fill{width:100%;height:100%}
.sketch-frame{position:absolute;border:3px solid var(--rose);background:var(--paper);padding:4px}
.sketch-frame .fill{width:100%;height:100%}

.service{position:absolute;font-size:9.4px;line-height:11.6px}
.service h3{font-weight:900;font-size:12.4px;line-height:14px;text-transform:uppercase;letter-spacing:.1px}
.service h3 .leader{font-weight:400;font-size:8px;letter-spacing:0}
.service h3 .price{font-weight:900;font-size:10.5px}
.service ul{list-style:none}
.service li{padding-left:10px;position:relative}
.service li::before{content:"";position:absolute;left:1px;top:4px;width:5px;height:5px;border-radius:50%;background:var(--ink)}

/* spread 2 */
.page--tan-photo{left:132px;top:505px;width:468px;height:470px}
.title-tab{position:absolute;left:286px;top:10px;width:162px;height:152px;background:var(--charcoal);border-radius:0 0 10px 10px;display:flex;flex-direction:column;justify-content:center;padding-left:16px}
.title-tab .light{color:#fff;font-weight:300;font-size:25px;letter-spacing:.5px;line-height:28px}
.title-tab .bold{color:var(--rose);font-weight:700;font-size:25px;letter-spacing:1.5px;line-height:30px}
.page--tan-text{left:600px;top:505px;width:468px;height:470px;background:var(--paper-warm)}
.stripe{position:absolute;left:0;width:100%}
.article{position:absolute;font-size:8.9px;line-height:10.9px}
.article h3{font-weight:900;font-size:12px;line-height:14px;text-transform:uppercase}
</style>
</head>
<body>

<!-- Page 11 -->
<section class="page page--eyes">
  <div class="photo-band"></div>

  <div class="photo-frame" style="left:322px;top:41px;width:136px;height:83px">
    <div class="fill" role="img" aria-label="Close-up van een oog met permanente eyeliner" style="background:linear-gradient(135deg,#b9876e,#7a5a4b 55%,#a77c68)"></div>
  </div>
  <div class="photo-frame" style="left:322px;top:190px;width:136px;height:83px">
    <div class="fill" role="img" aria-label="Close-up van een oog met brede eyeliner" style="background:linear-gradient(135deg,#c19079,#6e5548 55%,#b08472)"></div>
  </div>
  <div class="photo-frame" style="left:322px;top:325px;width:136px;height:83px">
    <div class="fill" role="img" aria-label="Close-up van een oog met fijne eyeliner en wimpers" style="background:linear-gradient(135deg,#8a5a8c,#4b3a55 55%,#c49aaa)"></div>
  </div>

  <div class="service" style="left:19px;top:42px;width:290px">
    <h3>Permanente make up volledige oogcontour<span class="leader"> ..................................</span><span class="price">€360</span></h3>
    <p>Je tekent al jarenlang een lijntje boven en onder uw oog?<br>Een perfecte vorm is nodig want dit vervangt wel degelijk uw make-up! Ik ben altijd eerlijk<br>en oprecht want uw mooie liner is mijn beste reclame!<br>Ik geef heel graag advies over de mogelijkheden.<br>Alles wordt uitvoerig besproken en uitgetekend zo ziet u al hoe uw eyeliner er zal uitzien en kan u zelf aangeven of u deze fijner of net iets dikker wenst.</p>
  </div>

  <div class="service" style="left:19px;top:191px;width:290px">
    <h3>Brede eyeliner boven het oog<span class="leader"> ............</span><span class="price">€235</span></h3>
    <p>Je tekent al jarenlang een “dikker” lijntje ?<br>Een perfecte vorm is nodig want dit vervangt wel degelijk uw make-up! Ik ben altijd eerlijk en oprecht want uw mooie liner is mijn beste reclame! Ik geef heel graag advies over de mogelijkheden.<br>Alles wordt uitvoerig besproken en uitgetekend zo ziet u al hoe uw eyeliner er zal uitzien en kan u zelf aangeven of u deze fijner of net iets dikker wenst.</p>
  </div>

  <div class="service" style="left:19px;top:325px;width:290px">
    <h3>Fijne eyeliner boven (wimperinvulling) het oog<span class="leader"> .....................</span><span class="price">€186</span></h3>
    <p>De fijne eyeliner of wimperinvulling om uw ogen op een subtiele manier iets meer accentueren en laten spreken!<br>Een eye-liner met subtiele klasse!<br>uw ogen zullen meer spreken en u hoeft zich geen zorgen meer te maken over uitgelopen lijntjes of panda ogen.<br>een echte Liner zonder het too much effect.</p>
  </div>

  <div class="page-number" style="right:0">11</div>
</section>

<!-- Page 12 -->
<section class="page page--brows">
  <div class="sketch-frame" style="left:10px;top:42px;width:136px;height:82px">
    <div class="fill" role="img" aria-label="Tekening van een wenkbrauw in hairstroke techniek" style="background:linear-gradient(180deg,#fff 30%,#e4e4e4 50%,#fff 70%)"></div>
  </div>
  <div class="sketch-frame" style="left:10px;top:190px;width:136px;height:82px">
    <div class="fill" role="img" aria-label="Tekening van een gepoederde wenkbrauw" style="background:linear-gradient(180deg,#fff 28%,#9a9a9a 48%,#fff 68%)"></div>
  </div>
  <div class="sketch-frame" style="left:10px;top:325px;width:136px;height:82px">
    <div class="fill" role="img" aria-label="Tekening van een power brow wenkbrauw" style="background:linear-gradient(180deg,#fff 30%,#b5b5b5 50%,#fff 70%)"></div>
  </div>

  <div class="service" style="left:162px;top:10px;width:290px">
    <h3>Wenkbrauwen hairstroke techniek<span class="leader"> .......................................................</span><span class="price">€320</span></h3>
    <p>voor wie?</p>
    <ul>
      <li>je wenst een hyper realistisch natuurlijk resultaat</li>
      <li>je hebt weinig tot geen eigen haartjes</li>
      <li>je bent het niet gewend om make up op je wenkbrauwen te gebruiken oplossing:</li>
      <li>er worden hairstrokes (fijne haartjes) gepigmenteerd op de huid</li>
      <li>voor een vollere wenkbrauw</li>
      <li>met een heel natuurlijke look</li>
    </ul>
  </div>

  <div class="service" style="left:162px;top:172px;width:290px">
    <h3>Wenkbrauwen shading brow of poederwenkbrauw<span class="leader"> ......................................</span><span class="price">€320</span></h3>
    <p>voor wie?</p>
    <ul>
      <li>je wil elke dag mooi gevormde wenkbrauwen</li>
      <li>je houdt van de soft make up look</li>
      <li>je hebt weinig tot voldoende eigen haartjes</li>
    </ul>
    <p>oplossing:</p>
    <ul>
      <li>intensere kleur geven aan de wenkbrauw</li>
      <li>mooie vorm geven aan de wenkbrauw</li>
      <li>voor een mooie, zachte make up look gezien bij Lena Marsh</li>
    </ul>
  </div>

  <div class="service" style="left:162px;top:333px;width:290px">
    <h3>Wenkbrauwen power brow<span class="leader"> .................</span><span class="price">€320</span></h3>
    <p>voor wie:</p>
    <ul>
      <li>je wenst een meer uitgesproken resultaat</li>
      <li>je draagt dagelijks make up aan de wenkbrauwen</li>
      <li>je hebt voldoende haartjes</li>
    </ul>
    <p>oplossing:</p>
    <ul>
      <li>shading techniek + hairstroke techniek = power brow</li>
      <li>voller maken van de eigen wenkbrauw</li>
      <li>meer kleur en vorm geven</li>
      <li>voor de echte make up look Gezien bij Nora Vale</li>
    </ul>
  </div>

  <div class="page-number" style="right:0">12</div>
</section>

<!-- Page 13 -->
<section class="page page--tan-photo">
  <div class="abs" role="img" aria-label="Vrouw met gebruinde huid in bikini, staand in zee" style="inset:0;background:linear-gradient(180deg,#6fa2c4 0%,#4f86a8 45%,#8cb7c4 75%,#c9a58a 100%)"></div>
  <div class="abs" style="left:447px;top:0;width:21px;height:4px;background:var(--blush)"></div>
  <div class="abs" style="left:447px;top:8px;width:21px;height:4px;background:var(--sky)"></div>
  <div class="title-tab">
    <span class="light">AIRBRUSH</span>
    <span class="bold">TANNING</span>
  </div>
</section>

<!-- Page 14 -->
<section class="page page--tan-text">
  <div class="stripe" style="top:0;height:5px;background:var(--blush)"></div>
  <div class="stripe" style="top:9px;height:6px;background:var(--blush-soft)"></div>
  <div class="stripe" style="top:19px;height:5px;background:var(--blush)"></div>
  <div class="abs" style="left:0;top:0;width:4px;height:28px;background:var(--sky)"></div>

  <div class="article" style="left:20px;top:44px;width:440px">
    <h3>De voorbereiding</h3>
    <p>De dag van de afspraak kan je beter geen vette of oliehoudende producten op het lichaam aanbrengen. Een goede scrubbeurt (op waterbasis, zonder olie !!) zal ervoor zorgen dat de kleur mooi egaal en gelijkmatig verdeeld wordt en belangrijker nog, dat je huid veel langer bruin zal blijven. De loszittende dode huidcellen worden verwijderd bij het scrubben. Degene die nog vast zitten zullen nog veel langer op hun plaats blijven. Opgelet : indien je zelf de scrub uitvoert, zorg ervoor dat je geen stukken vergeet !<br>
    Trek donkere loszittende kledij aan. Op lichte kledij kan de gekleurde component licht kleur afgeven. Dit laat zich volledig verwijderen in de was. De kledij mag niet spannen en vooral geen wrijving op de huid geven. De component die de uiteindelijke kleur moet geven werkt gedurende ongeveer 12 uur verder. Op plaatsen waar de kledij op de huid schuurt kan het product vroegtijdig weggewreven worden en dus lichtere strepen geven.<br>
    Het product laat geen vlekken na op de kledij. Alleen op de materialen van zeer fijne lingerie kan het het eventueel inwerken.<br>
    Het product werkt heel goed in op nagels (is een verhoorning van de huid en bestaat dus ook uit dode kernloze huidcellen) ! Wij proberen deze zo veel mogelijk te sparen bij het spuiten. Om helemaal zeker te zijn, vooral bij veelvuldige herhalingen, kan je beter je nagels lakken, eventueel met een kleurloze nagellak. Let wel op dat je geen huid bedekt met de lak.</p>
  </div>

  <div class="sketch-frame" style="left:20px;top:260px;width:130px;height:89px;padding:0">
    <div class="fill" role="img" aria-label="Airbrush pistool dat bruiningsproduct op een buik spuit" style="background:linear-gradient(90deg,#c98a6a,#e2b396 60%,#f3f0ee)"></div>
  </div>

  <div class="article" style="left:162px;top:260px;width:298px">
    <h3>De airbrush tanning zelf</h3>
    <p>Je huid wordt ingespoten met het product. Je ziet onmiddellijk het resultaat. Eventueel wordt in verschillende lagen gespoten zodat je zeker niet te bruin kan worden.<br>Het inspuiten van het volledig lichaam duurt ongeveer 10 minuten. Daarna moet je alvorens de kleren aan te trekken nog een kwartiertje het product laten indrogen. Je verlaat het instituut met een mooie, gezonde bruine kleur.</p>
  </div>

  <div class="article" style="left:20px;top:357px;width:440px">
    <h3>De nazorg</h3>
    <p>Gedurende de eerste 8 uren na de airbrush tanning kan je best voorkomen om hevig te zweten. Dus best geen sport of andere zware inspanningen. Je mag niet douchen ! Tijdens deze eerste 8 uren kan het product een lichte kleur afgeven op kledij of lakens. Deze verdwijnt zonder probleem in de was.Na 8 uur mag je douchen. De tijdelijke kleurcomponent spoelt volledig weg. Ondertussen heeft je huid een mooie bruine kleur gekregen.Hoe beter je je huid hydrateert hoe langer je de kleur kan behouden. Je kleur blijft gemiddeld tussen de 7 dagen en 10 dagen naargelang je huidtype.<br>Daarna begint de kleur te vervagen.</p>
  </div>

  <div class="page-number" style="right:0">14</div>
</section>

</body>
</html>
```